Book cover for a very impressive real-life healing story from a stage IV deadly disease

I need a book cover design for the French translation of the US book http://www.brelvantbooks.example/Linders-Journey-Through-Illness-Story/dp/0412298765/ref=sr_1_4?s=books&ie=UTF8&qid=1455100794&sr=1-4&keywords=tam+vesko
.
I do not want the word AIDS on the French cover, as the story of this book applies to any disease.

The french title will be something like :
Un matin nouveau !
Condamné par la médecine, il guérit grâce au jeûne, la détoxination, et l’amour.

which means something like
A new morning!
Subtitle : Given up by official medecine, he managed to heal with fasting, detox and love.

Many thanks !

Target Market(s)

Anybody interested in natural health

Requirements
Must have
• Nothing special
Nice to have
• Nothing special
Should not have
• Nothing special

```html
<!DOCTYPE html>
<html lang="fr">
<head>
<meta charset="utf-8">
<title>Un matin nouveau ! — Tam Vesko</title>
<link rel="stylesheet" href="https://fonts.googleapis.com/css2?family=Anton&family=Arimo:wght@400&display=swap">
<style>
  :root {
    --cover-bg: #000000;
    --title-red: #d7262e;
    --text-white: #ffffff;
    --leaf-green: #22b88a;
  }
  * { margin: 0; padding: 0; box-sizing: border-box; }
  html, body {
    width: 750px;
    height: 1200px;
    overflow: hidden;
    background: var(--cover-bg);
  }
  .cover {
    position: relative;
    width: 750px;
    height: 1200px;
    background: var(--cover-bg);
    overflow: hidden;
  }
  .cover-title {
    position: absolute;
    left: 0;
    top: 0;
    width: 750px;
    height: 520px;
  }
  .cover-title text {
    font-family: "Anton", "Impact", sans-serif;
    font-size: 255px;
    fill: var(--title-red);
  }
  .subtitle {
    position: absolute;
    left: 565px;
    top: 294px;
    font-family: "Anton", "Impact", sans-serif;
    font-size: 20px;
    line-height: 29.6px;
    color: var(--text-white);
    text-transform: uppercase;
    letter-spacing: 0;
  }
  .title-rule {
    position: absolute;
    left: 0;
    top: 526px;
    width: 750px;
    height: 7px;
    background: var(--title-red);
  }
  .author {
    position: absolute;
    left: 42px;
    top: 548px;
    font-family: "Arimo", "Arial", sans-serif;
    font-size: 45px;
    font-weight: 400;
    line-height: 52px;
    color: var(--text-white);
  }
  .rose-art {
    position: absolute;
    left: 272px;
    top: 634px;
    width: 450px;
    height: 562px;
    background: linear-gradient(180deg,
      rgba(215, 38, 46, 0.35) 0%,
      rgba(215, 38, 46, 0.22) 50%,
      rgba(34, 184, 138, 0.25) 75%,
      rgba(34, 184, 138, 0.12) 100%);
  }
</style>
</head>
<body>
  <main class="cover">
    <svg class="cover-title" viewBox="0 0 750 520" role="heading" aria-level="1" aria-label="Un matin nouveau !">
      <text x="48" y="255" textLength="660" lengthAdjust="spacingAndGlyphs">UN MATIN</text>
      <text x="48" y="485" textLength="482" lengthAdjust="spacingAndGlyphs">NOUVEAU !</text>
    </svg>

    <p class="subtitle">
      Condamné par<br>
      la médecine, il<br>
      guérit grâce<br>
      au jeûne,<br>
      la détoxination,<br>
      et l’amour
    </p>

    <div class="title-rule"></div>

    <p class="author">Tam Vesko</p>

    <div class="rose-art" role="img" aria-label="Line drawing of a red rose with a green stem and leaves"></div>
  </main>
</body>
</html>
```